依頼詳細
話題を呼んだり、涙がでてしまうほどのデザインを求めます。
※イメージを添付します。
記載項目
特になし
希望イメージ
シンプル 複雑
単色 カラフル
暗い 明るい
日常 高級
遊び心 厳粛
未来的 伝統的
女性的 男性的
希望する色
赤系、水色系、黄・オレンジ系
納品ファイル
補足説明
イメージとして参考資料を添付します。
どれも一度見たら忘れられない看板ばかりです!
おもしろい候補が複数発生した場合、当選者を増やします。

よろしくお願いいたします。
期間を1/5まで延長とさせていただきます。
年明けまで期間を延ばし、おもしろ提案を受けます。
非常におもしろいデザインが多数あり、選定するのに悩んでいるところがホンネです。
最終的に複数選定する可能性も十分にありますので、皆さん沢山提案を上げていただけると幸いです。
どうぞよろしくお願いいたします。
■ 選んだ理由

ご提案いただいたデザインの殆どがおもしろい提案でした。その中で特に的を得ていましたので、選ばせていただきました。

■ 提案者全員のお礼・コメント

どれも甲乙つけがたいデザインでした。ご提案ありがとうございました。
同じようなコンペを今後も開催していきたいと考えております。
是非お気に入りランサーに登録いただき見逃すことがないようにお願いします。

```html
<!DOCTYPE html>
<html lang="ja">
<head>
<meta charset="utf-8">
<title>部屋づき合いは人付き合いと同じくむずかしい。</title>
<link rel="stylesheet" href="https://fonts.googleapis.com/css2?family=Noto+Sans+JP:wght@700;900&display=swap">
<style>
  :root {
    --paper: #ffffff;
    --sign-yellow: #ffe100;
    --alert-red: #e60012;
    --ink: #111111;
    --scene-shade: #c9a800;
    --scene-dark: #6b5a00;
  }
  html, body {
    margin: 0;
    padding: 0;
    overflow: hidden;
    background: var(--paper);
  }
  .poster {
    position: relative;
    width: 846px;
    height: 1200px;
    background: var(--paper);
    overflow: hidden;
    font-family: "Noto Sans JP", sans-serif;
  }
  .sign-panel {
    position: absolute;
    left: 51px;
    top: 40px;
    width: 749px;
    height: 1007px;
    background: var(--sign-yellow);
    border-radius: 30px;
  }
  .headline {
    position: absolute;
    left: 175px;
    top: 178px;
    margin: 0;
    font-weight: 900;
    font-size: 60px;
    line-height: 95px;
    letter-spacing: 0.01em;
    color: var(--alert-red);
  }
  .headline span { display: block; white-space: nowrap; }
  .house-frame {
    position: absolute;
    left: 90px;
    top: 636px;
  }
  .scene-area {
    position: absolute;
    background: linear-gradient(135deg, var(--scene-dark), var(--scene-shade));
    border-radius: 6px;
  }
  .scene-bull {
    left: 132px;
    top: 758px;
    width: 176px;
    height: 92px;
  }
  .equals {
    position: absolute;
    left: 437px;
    top: 772px;
  }
  .scene-kick {
    left: 550px;
    top: 665px;
    width: 140px;
    height: 192px;
  }
  .tagline {
    position: absolute;
    left: 0;
    right: 0;
    top: 1088px;
    margin: 0;
    text-align: center;
    font-weight: 700;
    font-size: 34px;
    letter-spacing: 0.12em;
    color: var(--ink);
  }
</style>
</head>
<body>
  <main class="poster">
    <section class="sign-panel"></section>

    <h1 class="headline">
      <span>部屋づき合いは</span>
      <span>人付き合いと同じく</span>
      <span>むずかしい。</span>
    </h1>

    <svg class="house-frame" width="260" height="232" viewBox="0 0 260 232" aria-hidden="true">
      <path d="M6 108 L130 14 L254 108" fill="none" stroke="var(--ink)" stroke-width="14" stroke-linejoin="miter"/>
      <path d="M30 92 V222 H230 V92" fill="none" stroke="var(--ink)" stroke-width="12"/>
    </svg>
    <div class="scene-area scene-bull" role="img" aria-label="部屋の中で牛が人に突進しているピクトグラム"></div>

    <svg class="equals" width="70" height="44" viewBox="0 0 70 44" aria-hidden="true">
      <rect x="0" y="0" width="70" height="14" fill="var(--ink)"/>
      <rect x="0" y="30" width="70" height="14" fill="var(--ink)"/>
    </svg>

    <div class="scene-area scene-kick" role="img" aria-label="人が人を蹴り飛ばしているピクトグラム"></div>

    <p class="tagline">安心のお部屋探しは●●●へ!</p>
  </main>
</body>
</html>
```